I need a cover for a brochure made

I need a cover for a brochure. The dimensions are 8.25 wide and 5.25 high... I also need a .25 inch bleed outside of those dimensions.

I need it to look like a vintage photo album cover. In big words, I would like it to say "Family". Above it in smaller words "To our Carrowmere Paddle" ... making it look like the words are gold inlay or something.

I would like it kind of in the style of some of the attached maybe. Just vintage looking.

```html
<!DOCTYPE html>
<html lang="en">
<head>
<meta charset="utf-8">
<title>Family – Brochure Cover</title>
<link rel="stylesheet" href="https://fonts.googleapis.com/css2?family=Cinzel+Decorative:wght@700;900&family=Cinzel:wght@600;700&display=swap">
<style>
  :root {
    --backdrop: #d6d6d6;
    --leather: #4a1d13;
    --leather-deep: #3a140c;
    --leather-light: #55241a;
    --gold: #d9ae5c;
    --gold-light: #f3d48f;
    --gold-deep: #a77a2c;
    --paper-gold: #dcb466;
  }
  * { margin: 0; padding: 0; box-sizing: border-box; }
  html, body {
    width: 761px;
    height: 1200px;
    overflow: hidden;
    background: var(--backdrop);
  }
  .cover {
    position: absolute;
    left: 64px;
    top: 396px;
    width: 633px;
    height: 407px;
    background: radial-gradient(ellipse at 55% 45%, var(--leather-light), var(--leather) 55%, var(--leather-deep));
    overflow: hidden;
  }
  .spine {
    position: absolute;
    left: 0; top: 0;
    width: 66px; height: 100%;
    background: linear-gradient(90deg, #d3a955, var(--paper-gold) 40%, #e3bf73 80%, #c99d4b);
  }
  .spine-rule {
    position: absolute;
    left: 75px; top: 0;
    width: 1px; height: 100%;
    background: var(--gold);
  }
  .corner {
    position: absolute;
    right: 0;
    width: 110px; height: 110px;
  }
  .corner--top { top: 0; }
  .corner--bottom { bottom: 0; }
  .corner svg { display: block; width: 100%; height: 100%; }
  .ornament {
    position: absolute;
    background: linear-gradient(90deg, rgba(217,174,92,0), rgba(217,174,92,0.55) 30%, rgba(243,212,143,0.7) 50%, rgba(217,174,92,0.55) 70%, rgba(217,174,92,0));
    border-radius: 6px;
  }
  .ornament--top-rule { left: 206px; top: 28px; width: 208px; height: 14px; }
  .ornament--bottom-rule { left: 206px; top: 386px; width: 208px; height: 14px; }
  .ornament--title-rule { left: 236px; top: 274px; width: 228px; height: 20px; }
  .ornament--swirl {
    left: 320px; top: 102px; width: 80px; height: 50px;
    background: radial-gradient(ellipse, rgba(243,212,143,0.75), rgba(217,174,92,0.35) 60%, rgba(217,174,92,0) 75%);
    border-radius: 50%;
  }
  .gold-text {
    position: absolute;
    background: linear-gradient(180deg, var(--gold-light), var(--gold) 50%, var(--gold-deep));
    -webkit-background-clip: text;
    background-clip: text;
    color: transparent;
    white-space: nowrap;
    line-height: 1;
  }
  .title-lead {
    left: 228px; top: 116px;
    font-family: "Cinzel", serif;
    font-weight: 700;
    font-size: 26px;
  }
  .title-name {
    left: 268px; top: 156px;
    font-family: "Cinzel", serif;
    font-weight: 700;
    font-size: 21px;
  }
  .title-main {
    left: 160px; top: 180px;
    font-family: "Cinzel Decorative", serif;
    font-weight: 900;
    font-size: 88px;
    letter-spacing: 1px;
  }
</style>
</head>
<body>
  <main class="cover">
    <div class="spine"></div>
    <div class="spine-rule"></div>

    <div class="corner corner--top">
      <svg viewBox="0 0 110 110" role="img" aria-label="Gold corner guard with vine ornament along its edge">
        <polygon points="28,0 110,0 110,82" fill="#dcb466"/>
        <polygon points="14,0 28,0 110,82 110,96" fill="rgba(217,174,92,0.35)"/>
      </svg>
    </div>
    <div class="corner corner--bottom">
      <svg viewBox="0 0 110 110" role="img" aria-label="Gold corner guard with vine ornament along its edge">
        <polygon points="110,28 110,110 28,110" fill="#dcb466"/>
        <polygon points="110,14 110,28 28,110 14,110" fill="rgba(217,174,92,0.35)"/>
      </svg>
    </div>

    <div class="ornament ornament--top-rule" role="img" aria-label="Gold filigree divider"></div>
    <div class="ornament ornament--swirl" role="img" aria-label="Gold flourish swirl"></div>

    <h1 class="gold-text title-lead">To our</h1>
    <p class="gold-text title-name">Carrowmere Paddle</p>
    <p class="gold-text title-main">Family</p>

    <div class="ornament ornament--title-rule" role="img" aria-label="Gold filigree divider beneath the title"></div>
    <div class="ornament ornament--bottom-rule" role="img" aria-label="Gold filigree divider"></div>
  </main>
</body>
</html>
```